Business Card design for amazing new Dental Office

Please read this brief closely!

Our client is a modern new dental office/
They love their new logo.
Now it's time to create a business card for them.

It should be a two sided card:
Side one should have the logo and name and maybe a color background or design.
Side two should have all the contact information which is here:

Marcus Holloway, D.D.S
General and Cosmetic Dentistry
4187 W. Pinecrest Avenue
Ventura, CA 93011
(805) 912-4386
drmarcus@bluefernsmiles-example.com
www.bluefernsmiles-example.com

Feel free to arrange that info as you like and to style both sides of the card according to your creativity. This is a chance for you to show your design skills!

Client is open to font choices and is looking for a style that is amazing and premium. Colors can be selected from the logo, or any variation of those.

You will not win this contest with a less than beautiful card design so please feel free to make multiple submissions.

Logo files attached and please message me with any questions.
Thanks!

Target Market(s)

Families and Professionals seeking dental services

Industry/Entity Type

Dental

Contact Information for Business Card

Logo, style, contact info as per the brief

Font styles to use
Sans Serif

Requirements
Must have
• Client's logo and contact details as per brief
Nice to have
• Unique style reflecting high end dental clinic near the beach
Should not have
• Must not look like a template

```html
<!DOCTYPE html>
<html lang="en">
<head>
<meta charset="utf-8">
<title>Blue Fern Smiles – Business Card</title>
<link rel="stylesheet" href="https://fonts.googleapis.com/css2?family=Roboto:wght@400;500;700&display=swap">
<style>
  :root {
    --page: #e4e4e4;
    --navy: #2a2d40;
    --gold-yellow: #d3b84a;
    --gold-warm: #dea55c;
    --teal: #6dc3ba;
    --sky: #6fc5de;
    --blue: #47b1e5;
    --stripe-gold: #d6b04e;
    --fold: #6e3d12;
    --ink: #14202b;
    --accent-blue: #1a7fc4;
    --icon-blue: #3aa0dc;
    --pin-blue: #0d7ecb;
    --light: #e8e8ea;
  }
  html, body {
    margin: 0;
    padding: 0;
    width: 1080px;
    height: 1200px;
    overflow: hidden;
    background: var(--page);
    font-family: "Roboto", sans-serif;
  }
  .canvas { position: relative; width: 1080px; height: 1200px; }
  .card { position: absolute; display: block; }
  .card--front { left: 182px; top: 125px; width: 720px; height: 432px; }
  .card--back { left: 182px; top: 640px; width: 728px; height: 437px; }
  .card text { font-family: "Roboto", sans-serif; }
  .doctor-name { font-weight: 700; font-size: 56px; font-variant: small-caps; fill: var(--ink); }
  .doctor-name .first { fill: var(--accent-blue); }
  .specialty { font-size: 36px; fill: var(--ink); }
  .brand-name { font-weight: 500; font-size: 46px; letter-spacing: 3px; }
  .brand-name--dark { fill: var(--navy); }
  .brand-name--light { fill: var(--light); }
  .contact-line { font-size: 23px; fill: var(--ink); }
  .band-address { font-size: 33px; font-weight: 400; fill: var(--ink); }
</style>
</head>
<body>
<main class="canvas">

  <!-- Front side -->
  <svg class="card card--front" viewBox="0 0 1200 720" xmlns="http://www.w3.org/2000/svg" aria-label="Front of business card">
    <defs>
      <linearGradient id="frontGold" x1="0" x2="1" y1="0" y2="0">
        <stop offset="0" stop-color="var(--gold-yellow)"/>
        <stop offset="1" stop-color="var(--gold-warm)"/>
      </linearGradient>
      <linearGradient id="frontBand" x1="0" x2="1" y1="0" y2="0">
        <stop offset="0" stop-color="#cdb93e"/>
        <stop offset="1" stop-color="#dca65c"/>
      </linearGradient>
    </defs>
    <rect class="gold-field" width="1200" height="720" fill="url(#frontGold)"/>
    <g class="wave-stripes" fill="none">
      <path d="M752 0 C670 90,650 250,720 380 S790 600,650 720" stroke="var(--blue)" stroke-width="44"/>
      <path d="M717 0 C635 90,615 250,685 380 S755 600,615 720" stroke="var(--stripe-gold)" stroke-width="32"/>
      <path d="M687 0 C605 90,585 250,655 380 S725 600,585 720" stroke="var(--sky)" stroke-width="32"/>
      <path d="M657 0 C575 90,555 250,625 380 S695 600,555 720" stroke="var(--stripe-gold)" stroke-width="32"/>
      <path d="M627 0 C545 90,525 250,595 380 S665 600,525 720" stroke="var(--teal)" stroke-width="32"/>
    </g>
    <path class="navy-field" d="M0 0 L605 0 C523 90,503 250,573 380 S643 600,503 720 L0 720 Z" fill="var(--navy)"/>
    <polygon class="band-fold" points="665,260 717,260 635,318" fill="var(--fold)"/>
    <polygon class="name-band" points="0,105 683,105 717,260 0,260" fill="url(#frontBand)"/>
    <text class="doctor-name" x="105" y="180"><tspan class="first">Marcus</tspan> Holloway, D.D.S</text>
    <text class="specialty" x="105" y="224">General and Cosmetic Dentistry</text>
    <text class="brand-name brand-name--dark" x="918" y="395" text-anchor="middle">Blue Fern Smiles</text>
  </svg>

  <!-- Back side -->
  <svg class="card card--back" viewBox="0 0 1213 728" xmlns="http://www.w3.org/2000/svg" aria-label="Back of business card">
    <defs>
      <linearGradient id="backGold" x1="0" x2="1" y1="0" y2="0">
        <stop offset="0" stop-color="var(--gold-warm)"/>
        <stop offset="1" stop-color="var(--gold-yellow)"/>
      </linearGradient>
      <linearGradient id="backBand" x1="0" x2="1" y1="0" y2="0">
        <stop offset="0" stop-color="#dca65c"/>
        <stop offset="1" stop-color="#cdb93e"/>
      </linearGradient>
    </defs>
    <rect class="gold-field" width="1213" height="728" fill="url(#backGold)"/>
    <g class="wave-stripes" fill="none">
      <path d="M637 0 C560 80,520 250,580 420 S600 640,537 728" stroke="var(--blue)" stroke-width="44"/>
      <path d="M672 0 C595 80,555 250,615 420 S635 640,572 728" stroke="var(--stripe-gold)" stroke-width="32"/>
      <path d="M702 0 C625 80,585 250,645 420 S665 640,602 728" stroke="var(--sky)" stroke-width="32"/>
      <path d="M732 0 C655 80,615 250,675 420 S695 640,632 728" stroke="var(--stripe-gold)" stroke-width="32"/>
      <path d="M762 0 C685 80,645 250,705 420 S725 640,662 728" stroke="var(--teal)" stroke-width="32"/>
    </g>
    <path class="navy-field" d="M797 0 C720 80,680 250,740 420 S760 640,697 728 L1213 728 L1213 0 Z" fill="var(--navy)"/>
    <polygon class="band-fold" points="583,464 637,464 637,430" fill="var(--fold)"/>
    <polygon class="address-band" points="583,464 1213,464 1213,622 618,622" fill="url(#backBand)"/>

    <g class="band-pin" transform="translate(660 509)">
      <rect width="68" height="68" rx="8" fill="var(--pin-blue)"/>
      <path d="M34 58 C24 44,18 36,18 27 A16 16 0 0 1 50 27 C50 36,44 44,34 58 Z" fill="#fff"/>
      <circle cx="34" cy="27" r="7" fill="var(--pin-blue)"/>
    </g>
    <text class="band-address" x="742" y="537">4187 W. Pinecrest Avenue</text>
    <text class="band-address" x="742" y="576">Ventura, CA 93011</text>

    <g class="contact-list">
      <g class="contact-icon" transform="translate(105 229)">
        <rect width="34" height="34" rx="5" fill="var(--icon-blue)"/>
        <path d="M17 28 C12 21,9 17,9 13 A8 8 0 0 1 25 13 C25 17,22 21,17 28 Z" fill="#fff"/>
        <circle cx="17" cy="13" r="3" fill="var(--icon-blue)"/>
      </g>
      <text class="contact-line" x="150" y="245">4187 W. Pinecrest Avenue,</text>
      <text class="contact-line" x="150" y="272">Ventura, CA 93011</text>

      <g class="contact-icon" transform="translate(105 306)">
        <rect width="34" height="34" rx="5" fill="var(--icon-blue)"/>
        <path d="M10 9 L14 8 L16 13 L13.5 15 C15 18.5,16.5 20,19.5 21.5 L21.5 19 L26.5 21 L25.5 25 C17 26,9 18,10 9 Z" fill="#fff"/>
      </g>
      <text class="contact-line" x="150" y="331">(805) 912-4386</text>

      <g class="contact-icon" transform="translate(105 388)">
        <rect width="34" height="34" rx="5" fill="var(--icon-blue)"/>
        <rect x="8" y="12" width="18" height="13" rx="2" fill="none" stroke="#fff" stroke-width="2"/>
        <path d="M13 12 V9 H21 V12 M8 17 H26" fill="none" stroke="#fff" stroke-width="2"/>
      </g>
      <text class="contact-line" x="150" y="413">drmarcus@bluefernsmiles-example.com</text>

      <g class="contact-icon" transform="translate(105 470)">
        <rect width="34" height="34" rx="5" fill="var(--icon-blue)"/>
        <g fill="none" stroke="#fff" stroke-width="1.8">
          <circle cx="17" cy="17" r="9"/>
          <ellipse cx="17" cy="17" rx="4" ry="9"/>
          <path d="M8 17 H26 M10 12 H24 M10 22 H24"/>
        </g>
      </g>
      <text class="contact-line" x="150" y="495">www.bluefernsmiles-example.com</text>
    </g>

    <text class="brand-name brand-name--light" x="927" y="330" text-anchor="middle">Blue Fern Smiles</text>
  </svg>

</main>
</body>
</html>
```